BW Law Firm Needs Sharp Letterhead

Our law firm recently selected a new logo through Pixelfair. Now we need a sharp Letterhead using the Letterhead.

Target Market(s)

Legal community, business clients

Industry/Entity Type

Law Firm

Requirements
Must have
• Our Logo
• Gordon P. Ashby
• Board Certified
• Civil Trial Law
• Ohio Council of Counsel Accreditation
• gashby@bwlegalteam.com
• 2715-C West 6th
• McAllen, TX 78599
• 555-213-0476
• www.bwlegalteam.com

```html
<!DOCTYPE html>
<html lang="en">
<head>
<meta charset="utf-8">
<title>BW Law Firm Letterhead</title>
<link href="https://fonts.googleapis.com/css2?family=Cinzel:wght@400;500&family=Quicksand:wght@500;600&display=swap" rel="stylesheet">
<style>
  :root {
    --backdrop: #e6e6e6;
    --paper: #f4f4f4;
    --ink: #4a4a4a;
    --ink-soft: #7a7a7a;
    --ghost: #e2e2e2;
    --band-dark: #3a3a3a;
    --band-light: #8a8a8a;
  }
  * { margin: 0; padding: 0; box-sizing: border-box; }
  html, body { width: 1200px; height: 936px; overflow: hidden; background: var(--backdrop); }
  .sheet {
    position: absolute; left: 300px; top: 40px;
    width: 605px; height: 856px;
    background: var(--paper);
    box-shadow: 0 2px 10px rgba(0,0,0,0.12);
  }
  .brand {
    position: absolute; left: 48px; top: 62px;
    display: flex; align-items: center; gap: 10px;
  }
  .brand-square { width: 30px; height: 30px; background: var(--ink); }
  .brand-text { display: flex; flex-direction: column; }
  .brand-name {
    font-family: "Cinzel", serif; font-weight: 500; font-size: 22px;
    letter-spacing: 0.5px; color: var(--ink);
    border-bottom: 1px solid var(--ink); padding-bottom: 2px;
  }
  .brand-tagline {
    font-family: "Cinzel", serif; font-weight: 400; font-size: 10.5px;
    letter-spacing: 1.2px; color: var(--ink-soft); margin-top: 3px;
  }
  .contact {
    position: absolute; right: 48px; top: 48px;
    font-family: "Quicksand", sans-serif; font-weight: 500; font-style: normal;
    font-size: 9px; line-height: 13px; text-align: right; color: var(--ink);
  }
  .contact .attorney { font-weight: 600; }
  .contact .credential { color: var(--ink-soft); }
  .contact .gap { display: block; height: 5px; }
  .watermark {
    position: absolute; left: 130px; top: 290px;
    width: 345px; height: 345px; border-radius: 18px;
    background: var(--ghost);
  }
  .footer-band {
    position: absolute; left: 0; right: 0; bottom: 0; height: 14px;
    display: flex;
  }
  .footer-band .band-light { flex: 0 0 58%; background: var(--band-light); }
  .footer-band .band-dark { flex: 1; background: var(--band-dark); }
</style>
</head>
<body>
  <main class="sheet">
    <header class="brand">
      <div class="brand-square"></div>
      <div class="brand-text">
        <span class="brand-name">Brightwell Webb</span>
        <span class="brand-tagline">Attorneys and Counselors</span>
      </div>
    </header>
    <address class="contact">
      <span class="attorney">Gordon P. Ashby</span><br>
      <span class="credential">Board Certified – Civil Trial Law</span><br>
      <span class="credential">Ohio Council of Counsel Accreditation</span>
      <span class="gap"></span>
      2715-C West 6th<br>
      McAllen, TX 78599<br>
      T: 555-213-0476<br>
      gashby@bwlegalteam.com<br>
      www.bwlegalteam.com
    </address>
    <div class="watermark" aria-hidden="true"></div>
    <footer class="footer-band">
      <div class="band-light"></div>
      <div class="band-dark"></div>
    </footer>
  </main>
</body>
</html>
```